Design few pages for professional development app

I need a website design for a prototype project. The goal of the project is to prototype a few basic screens for a professional development application.

The final design should be clean, modern, and appeal to a professional millenial clientele.The designs have been wireframed (see attached), and we'd like these wireframes converted to design files.

Here is the list of goals and tasks that correspond to the design: https://sheets.plorvane.com/grid/d/7kQWm48p3XZvrt2bYH5LcNaeJoTsUDfi82GhKxMp/edit?view=shared

Number of Pages Required

5+ page

Font styles to use
Serif
Sans Serif

Colors

Designer to choose colors to be used in the design.

Requirements
Nice to have
• Uses Google Material Design, Bootstrap, or another framework

```html
<!DOCTYPE html>
<html lang="en">
<head>
<meta charset="utf-8">
<title>Stepwell – Take Control of your Career</title>
<link rel="stylesheet" href="https://fonts.googleapis.com/css2?family=Barlow+Semi+Condensed:ital,wght@0,300;0,400;0,500;1,400&family=Caprasimo&display=swap">
<style>
  :root {
    --bg-top: #8c5d3c;
    --bg-upper: #95564a;
    --bg-mid: #8a3a55;
    --bg-low: #6e2548;
    --bg-bottom: #3f1a38;
    --text: #ffffff;
    --accent-yellow: #f5c542;
    --button: #5aaef5;
    --avatar-warm: #d9a58a;
    --avatar-cool: #b9b4b0;
  }
  * { margin: 0; padding: 0; box-sizing: border-box; }
  html, body {
    width: 1200px;
    height: 621px;
    overflow: hidden;
  }
  body {
    position: relative;
    font-family: "Barlow Semi Condensed", "Arial Narrow", sans-serif;
    color: var(--text);
  }
  .hero-backdrop {
    position: absolute;
    inset: 0;
    background:
      radial-gradient(ellipse 180px 320px at 600px 230px, rgba(240,150,120,0.45), transparent 70%),
      linear-gradient(180deg, var(--bg-top) 0%, var(--bg-upper) 25%, var(--bg-mid) 55%, var(--bg-low) 78%, var(--bg-bottom) 100%);
  }
  .site-header {
    position: absolute;
    top: 0; left: 0; right: 0;
    height: 70px;
  }
  .brand {
    position: absolute;
    left: 25px;
    top: 16px;
    font-weight: 300;
    font-size: 42px;
    line-height: 1;
    letter-spacing: 0.2px;
  }
  .search-toggle {
    position: absolute;
    right: 15px;
    top: 27px;
    width: 16px;
    height: 16px;
  }
  .hero-copy {
    position: absolute;
    left: 0; right: 0;
    top: 236px;
    text-align: center;
  }
  .hero-title {
    font-family: "Caprasimo", Georgia, serif;
    font-weight: 400;
    font-size: 31px;
    line-height: 38px;
    letter-spacing: 0.3px;
  }
  .hero-lead {
    font-size: 13.5px;
    line-height: 18px;
    margin-top: 1px;
    letter-spacing: 0.3px;
  }
  .hero-prompt {
    margin-top: 6px;
    font-size: 14px;
    line-height: 18px;
    font-style: italic;
    color: var(--accent-yellow);
  }
  .hero-note {
    font-size: 13.5px;
    line-height: 16px;
    letter-spacing: 0.3px;
  }
  .cta-button {
    display: inline-block;
    margin-top: 11px;
    width: 116px;
    height: 34px;
    line-height: 34px;
    border-radius: 17px;
    background: var(--button);
    color: var(--text);
    font-weight: 500;
    font-size: 14px;
    letter-spacing: 1px;
    text-decoration: none;
    box-shadow: 0 3px 8px rgba(0,0,0,0.25);
  }
  .testimonials {
    position: absolute;
    top: 463px;
    left: 0; right: 0;
  }
  .testimonial {
    position: absolute;
    top: 0;
    width: 320px;
    text-align: center;
  }
  .testimonial--left { left: 239px; }
  .testimonial--right { left: 639px; }
  .testimonial-avatar {
    width: 62px;
    height: 62px;
    border-radius: 50%;
    margin: 0 auto;
    border: 2px solid rgba(255,255,255,0.9);
  }
  .testimonial--left .testimonial-avatar { background: radial-gradient(circle at 50% 45%, var(--avatar-warm), #c2602f); }
  .testimonial--right .testimonial-avatar { background: radial-gradient(circle at 50% 45%, var(--avatar-cool), #6e6660); }
  .testimonial-quote {
    margin-top: 11px;
    font-size: 13.5px;
    line-height: 18px;
    letter-spacing: 0.3px;
  }
  .testimonial-author {
    font-size: 13.5px;
    line-height: 18px;
    font-style: italic;
  }
</style>
</head>
<body>
  <div class="hero-backdrop" role="img" aria-label="Background photo: a woman with a briefcase walking toward a glowing upward arrow, with arrows pointing left and right on a wall"></div>

  <header class="site-header">
    <div class="brand">Stepwell</div>
    <svg class="search-toggle" viewBox="0 0 16 16" aria-label="Search">
      <circle cx="6.5" cy="6.5" r="4.7" fill="none" stroke="#fff" stroke-width="2.4"/>
      <line x1="10" y1="10" x2="14.5" y2="14.5" stroke="#fff" stroke-width="2.8" stroke-linecap="round"/>
    </svg>
  </header>

  <main class="hero-copy">
    <h1 class="hero-title">Take Control of your Career</h1>
    <p class="hero-lead">Complete short, actionable tasks guaranteed to get you further in your career, faster than ever.</p>
    <p class="hero-prompt">Ready to get started?</p>
    <p class="hero-note">Take the short quiz below and get your personalized path today.</p>
    <a class="cta-button" href="#">GET STARTED</a>
  </main>

  <section class="testimonials">
    <figure class="testimonial testimonial--left">
      <div class="testimonial-avatar" role="img" aria-label="Portrait photo of a smiling red-haired woman"></div>
      <blockquote class="testimonial-quote">I love how quickly I can do the tasks,&amp; see progress.</blockquote>
      <figcaption class="testimonial-author">-Clara Whitfield</figcaption>
    </figure>
    <figure class="testimonial testimonial--right">
      <div class="testimonial-avatar" role="img" aria-label="Portrait photo of a dark-haired man in a shirt"></div>
      <blockquote class="testimonial-quote">The best investment I've made in myself in ages.</blockquote>
      <figcaption class="testimonial-author">-Theo Marsh</figcaption>
    </figure>
  </section>
</body>
</html>
```